Construction Company Website

I need a website for my construction company
Target Market(s)
People looking for construction work
Coding
Coded - Design and coding required
Number of Pages Required
4 page
Colors
0455a3
ffc214
Requirements
Must have
- A home page about my company,
A completed projects page showcasing some completed works
A contact me page with an enquiry form
Nice to have
- Professional and contemporary whilst classy website.

```html
<!DOCTYPE html>
<html lang="en">
<head>
<meta charset="utf-8">
<title>RW Construction</title>
<link href="https://fonts.googleapis.com/css2?family=Roboto:wght@400;500;700&family=Open+Sans:ital,wght@0,300;0,400;0,600;0,700;1,300;1,400&display=swap" rel="stylesheet">
<style>
:root{
  --navy:#0f1e33;
  --navy-deep:#16243a;
  --ink:#1b2a44;
  --gold:#ffc214;
  --gold-deep:#f4b400;
  --text:#2f3542;
  --light:#f5f5f5;
  --white:#ffffff;
}
*{box-sizing:border-box;margin:0;padding:0}
html,body{width:1200px;height:3586px;overflow:hidden;background:var(--white)}
body{font-family:"Open Sans",sans-serif;color:var(--text)}
.page{position:relative;width:1200px;height:3586px;overflow:hidden}
.abs{position:absolute}
.center{left:0;width:1200px;text-align:center}

.site-header{position:absolute;left:0;top:0;width:1200px;height:117px;background:var(--navy)}
.brand{position:absolute;left:111px;top:40px;display:flex;align-items:center;gap:10px}
.brand-mark{width:26px;height:26px;background:var(--gold-deep)}
.brand-name{font-weight:600;font-size:15px;letter-spacing:2px;color:var(--gold-deep)}
.main-nav a{position:absolute;top:51px;font-weight:600;font-size:14px;color:var(--white);text-decoration:none;letter-spacing:.2px}
.main-nav a.active{color:var(--gold)}
.main-nav a.active::after{content:"";position:absolute;left:-3px;right:-3px;bottom:-8px;height:3px;background:var(--gold)}

.hero{position:absolute;left:0;top:117px;width:1200px;height:587px;background:linear-gradient(180deg,#6d6a63 0%,#5a5146 30%,#7a6a56 60%,#6a5a48 100%)}
.hero-title{top:303px;font-family:"Roboto",sans-serif;font-weight:700;font-size:80px;color:var(--white);letter-spacing:1px;line-height:90px}
.hero-sub{top:395px;font-size:20px;color:var(--white)}
.hero-dots{top:654px;left:568px;display:flex;gap:5px}
.hero-dots span{width:12px;height:12px;border-radius:50%;background:rgba(255,255,255,.45)}
.hero-dots span.on{background:var(--gold)}

.section-title{font-family:"Roboto",sans-serif;font-weight:700;font-size:35px;color:var(--ink);letter-spacing:.2px}
.btn{position:absolute;display:block;background:var(--gold);color:var(--white);font-weight:700;font-size:14px;text-align:center;border-radius:5px;text-decoration:none}

.welcome{position:absolute;left:0;top:704px;width:1200px;height:418px;background:linear-gradient(180deg,#f7f7f7,#eeeeee)}
.welcome p{position:absolute;left:180px;width:840px;text-align:center;font-size:14.5px;line-height:23px;color:var(--text)}

.services{position:absolute;left:0;top:1122px;width:1200px;height:532px;background:var(--white)}
.service{position:absolute;top:0;width:190px;text-align:center}
.service svg{display:block;margin:0 auto}
.service h3{font-family:"Roboto",sans-serif;font-weight:400;font-size:16px;color:var(--ink);margin-top:6px}
.service p{font-size:12px;line-height:18px;color:var(--text);margin:10px auto 0;width:168px}

.reviews{position:absolute;left:0;top:1654px;width:1200px;height:523px;background:linear-gradient(180deg,#d9ae3a,#e6b83c)}
.avatar{position:absolute;left:536px;top:1783px;width:128px;height:128px;border-radius:50%;border:5px solid #f2e3b8;background:linear-gradient(160deg,#c9ccd0,#8a7f78)}
.quote{top:1934px;left:230px;width:740px;text-align:center;font-style:italic;font-weight:300;font-size:15px;line-height:23px;color:var(--white)}
.quote-mark{position:absolute;font-family:Georgia,serif;font-size:44px;line-height:44px;color:rgba(255,255,255,.55);font-style:italic}
.reviewer{top:2025px;font-weight:700;font-size:16px;color:var(--white)}
.reviewer-role{top:2052px;font-size:15px;color:var(--white)}
.review-dots{top:2124px;left:564px;display:flex;gap:10px}
.review-dots span{width:7px;height:7px;border-radius:50%;background:rgba(255,255,255,.6)}
.review-dots span.on{background:var(--gold)}

.projects{position:absolute;left:0;top:2177px;width:1200px;height:904px;background:var(--light)}
.projects-intro{top:2288px;left:200px;width:800px;text-align:center;font-size:14.5px;line-height:21px;color:var(--text)}
.project{position:absolute;width:314px;height:250px}

.site-footer{position:absolute;left:0;top:3081px;width:1200px;height:505px;background:var(--navy-deep)}
.footer-title{font-family:"Roboto",sans-serif;font-weight:500;font-size:28px;color:var(--white)}
.field{position:absolute;left:166px;width:396px;border:1px solid #4d5a70;color:#cfd5de;font-size:14px;padding:8px 13px}
.loc-head{font-weight:600;font-size:15px;color:var(--white)}
.loc-item{display:flex;align-items:center;gap:13px;font-size:14px;color:#d9dee6}
.loc-item svg{flex:none}
.copyright{left:111px;top:3548px;font-size:12px;color:var(--white)}
.footer-nav a{position:absolute;top:3550px;font-size:10px;color:#8c96a6;text-decoration:none}
</style>
</head>
<body>
<div class="page">

  <header class="site-header">
    <div class="brand"><span class="brand-mark"></span><span class="brand-name">RW CONSTRUCTION</span></div>
    <nav class="main-nav">
      <a class="active" style="left:379px" href="#">HOME</a>
      <a style="left:467px" href="#">ABOUT US</a>
      <a style="left:586px" href="#">PROJECTS</a>
      <a style="left:698px" href="#">SERVICES</a>
      <a style="left:808px" href="#">BLOG</a>
      <a style="left:893px" href="#">REVIEWS</a>
      <a style="left:999px" href="#">CONTACT US</a>
    </nav>
  </header>

  <section class="hero" role="img" aria-label="Photo of a building site with a laid patio base and houses behind"></section>
  <svg class="abs" style="left:42px;top:348px" width="20" height="34" viewBox="0 0 20 34"><path d="M17 2 3 17l14 15" fill="none" stroke="rgba(255,255,255,.7)" stroke-width="2"/></svg>
  <svg class="abs" style="left:1126px;top:348px" width="20" height="34" viewBox="0 0 20 34"><path d="M3 2l14 15L3 32" fill="none" stroke="rgba(255,255,255,.7)" stroke-width="2"/></svg>
  <h1 class="abs center hero-title">RW CONSTRUCTION</h1>
  <p class="abs center hero-sub">Excepteur sint occaecat cupidatat non proident sunt in culpa qui officia</p>
  <div class="abs hero-dots"><span class="on"></span><span></span><span></span><span></span></div>

  <section class="welcome">
    <h2 class="abs center section-title" style="top:68px">WELCOME TO RW CONSTRUCTION</h2>
    <p style="top:138px">Lorem ipsum dolor sit amet, consectetur adipiscing elit, sed do eiusmod tempor incididunt ut labore et dolore magna aliqua. Ut enim ad minim veniam, quis nostrud exercitation ullamco laboris nisi ut aliquip ex ea commodo.</p>
    <p style="top:211px">Sed ut perspiciatis unde omnis iste natus error sit voluptatem accusantium doloremque laudantium, totam rem aperiam, eaque ipsa quae ab illo inventore veritatis et quasi architecto beatae vitae dicta sunt explicabo.</p>
    <a class="btn" href="#" style="left:534px;top:313px;width:133px;height:39px;line-height:39px">READ MORE</a>
  </section>

  <section class="services">
    <h2 class="abs center section-title" style="top:50px">OUR SERVICES</h2>
    <div class="service" style="left:96px;top:126px">
      <svg width="150" height="150" viewBox="0 0 150 150"><rect x="31" y="31" width="88" height="88" transform="rotate(45 75 75)" fill="none" stroke="var(--gold-deep)" stroke-width="2"/><path d="M58 74 75 58l17 16M62 71v20h26V71M70 91V79h10v12" fill="none" stroke="var(--gold-deep)" stroke-width="2"/></svg>
      <h3>Painting</h3>
      <p>Lorem ipsum dolor sit amet, consectetur adipiscing elit, dunt ut labore et dolore</p>
    </div>
    <div class="service" style="left:300px;top:126px">
      <svg width="150" height="150" viewBox="0 0 150 150"><rect x="31" y="31" width="88" height="88" transform="rotate(45 75 75)" fill="none" stroke="var(--gold-deep)" stroke-width="2"/><path d="M58 64h36M56 72h36M54 80h36M52 88h36M70 64l-2 8M80 72l-2 8M66 80l-2 8" fill="none" stroke="var(--gold-deep)" stroke-width="2"/></svg>
      <h3>Carpentry and Siding</h3>
      <p>Lorem ipsum dolor sit amet, consectetur adipiscing elit, dunt ut labore et dolore</p>
    </div>
    <div class="service" style="left:505px;top:126px">
      <svg width="150" height="150" viewBox="0 0 150 150"><rect x="31" y="31" width="88" height="88" transform="rotate(45 75 75)" fill="var(--gold-deep)"/><path d="M60 95V72h14v23M66 95v-8h4v8M84 95V56M78 60h24M96 60v10M56 95h42M84 64l8-4" fill="none" stroke="var(--white)" stroke-width="2"/></svg>
      <h3>Construction</h3>
      <p>Lorem ipsum dolor sit amet, consectetur adipiscing elit, dunt ut labore et dolore</p>
    </div>
    <div class="service" style="left:710px;top:126px">
      <svg width="150" height="150" viewBox="0 0 150 150"><rect x="31" y="31" width="88" height="88" transform="rotate(45 75 75)" fill="none" stroke="var(--gold-deep)" stroke-width="2"/><path d="M54 88c4-18 10-26 21-26s17 8 21 26zM56 78h38M54 88h42M66 62l-4 26M75 62v26M84 62l4 26" fill="none" stroke="var(--gold-deep)" stroke-width="2"/></svg>
      <h3>Architecture Design</h3>
      <p>Lorem ipsum dolor sit amet, consectetur adipiscing elit, dunt ut labore et dolore</p>
    </div>
    <div class="service" style="left:914px;top:126px">
      <svg width="150" height="150" viewBox="0 0 150 150"><rect x="31" y="31" width="88" height="88" transform="rotate(45 75 75)" fill="none" stroke="var(--gold-deep)" stroke-width="2"/><path d="M63 56h24v38H63zM68 62h6v5h-6zM76 62h6v5h-6zM68 72h6v5h-6zM76 72h6v5h-6zM72 94v-9h6v9" fill="none" stroke="var(--gold-deep)" stroke-width="2"/></svg>
      <h3>House Renovation</h3>
      <p>Lorem ipsum dolor sit amet, consectetur adipiscing elit, dunt ut labore et dolore</p>
    </div>
    <a class="btn" href="#" style="left:517px;top:422px;width:167px;height:39px;line-height:39px">VIEW ALL SERVICES</a>
  </section>

  <section class="reviews" role="img" aria-label="Golden tinted photo of brick houses behind the reviews"></section>
  <h2 class="abs center section-title" style="top:1716px;color:var(--white)">CLIENT REVIEWS</h2>
  <div class="avatar" role="img" aria-label="Portrait of the reviewing client"></div>
  <span class="quote-mark" style="left:190px;top:1926px">&ldquo;</span>
  <p class="abs quote">At vero eos et accusamus et iusto odio dignissimos ducimus qui blanditiis praesentium voluptatum deleniti atque corrupti quos dolores et quas molestias excepturi sint occaecati cupiditate non provident, similique sunt in culpa qui officia deserunt mollitia animi, id est laborum et dolorum fuga.</p>
  <span class="quote-mark" style="left:832px;top:1986px">&rdquo;</span>
  <p class="abs center reviewer">BLANDITIIS PRAESENTI</p>
  <p class="abs center reviewer-role">(NAM LIBERO TEMPORE)</p>
  <div class="abs review-dots"><span class="on"></span><span></span><span></span><span></span></div>

  <section class="projects">
    <h2 class="abs center section-title" style="top:56px">OUR PROJECTS</h2>
  </section>
  <p class="abs projects-intro">Nam libero tempore, cum soluta nobis est eligendi optio cumque nihil impedit quo minus id quod maxime placeat facere possimus, omnis voluptas assumenda est, omnis dolor repellendus</p>
  <div class="project" style="left:111px;top:2365px;background:linear-gradient(180deg,#4f6b3a 0%,#7a8a6a 35%,#b9bcbd 60%,#a6a9ab 100%)" role="img" aria-label="Grey stone patio in a fenced garden"></div>
  <div class="project" style="left:443px;top:2365px;background:linear-gradient(90deg,#8a4a35 0%,#a55a3f 40%,#c2bcb4 70%,#8f9aa5 100%)" role="img" aria-label="Brick house front with blue door and gravel path"></div>
  <div class="project" style="left:774px;top:2365px;background:linear-gradient(180deg,#7fa8d8 0%,#3f6b34 40%,#8a7d6a 70%,#6e7c8c 100%)" role="img" aria-label="Garden cabin with new deck and paving"></div>
  <div class="project" style="left:111px;top:2637px;background:linear-gradient(180deg,#4e5b3a 0%,#8f7d63 25%,#2e9ee0 45%,#9a8a72 75%,#a7a6a2 100%)" role="img" aria-label="Newly built swimming pool with stone surround"></div>
  <div class="project" style="left:443px;top:2637px;background:linear-gradient(180deg,#9cc0e8 0%,#3d5e33 35%,#8a6a4e 55%,#5f8a3c 100%)" role="img" aria-label="Timber fence around a paved area on a lawn"></div>
  <div class="project" style="left:774px;top:2637px;background:linear-gradient(180deg,#a65c3e 0%,#b66a48 45%,#8a5a42 70%,#6e6a5a 100%)" role="img" aria-label="Prepared ground beside a brick house extension"></div>
  <a class="btn" href="#" style="left:534px;top:2956px;width:133px;height:39px;line-height:39px">VIEW MORE</a>

  <footer class="site-footer"></footer>
  <h2 class="abs footer-title" style="left:166px;top:3136px">QUICK SEND US MESSAGE</h2>
  <p class="abs" style="left:168px;top:3176px;font-size:12.5px;color:#dfe3ea">Sed ut perspiciatis unde omnis iste natus error sit voluptatem ...</p>
  <div class="field" style="top:3213px;height:34px">Name</div>
  <div class="field" style="top:3266px;height:34px">Email</div>
  <div class="field" style="top:3316px;height:110px">Message</div>
  <a class="btn" href="#" style="left:164px;top:3444px;width:98px;height:36px;line-height:36px;font-size:15px">SEND</a>

  <h2 class="abs footer-title" style="left:706px;top:3136px">LOCATIONS</h2>
  <div class="abs" style="left:708px;top:3192px">
    <p class="loc-head">Praesentium</p>
    <div style="margin-top:11px;display:grid;row-gap:6px">
      <div class="loc-item"><svg width="12" height="12" viewBox="0 0 12 12"><circle cx="6" cy="6" r="6" fill="#fff"/><path d="M3 6h5M6 3.5 8.5 6 6 8.5" fill="none" stroke="var(--navy-deep)" stroke-width="1.6"/></svg>Recusandae</div>
      <div class="loc-item"><svg width="12" height="12" viewBox="0 0 12 12"><circle cx="6" cy="6" r="6" fill="#fff"/><path d="M3 6h5M6 3.5 8.5 6 6 8.5" fill="none" stroke="var(--navy-deep)" stroke-width="1.6"/></svg>Itaque</div>
      <div class="loc-item"><svg width="12" height="12" viewBox="0 0 12 12"><circle cx="6" cy="6" r="6" fill="#fff"/><path d="M3 6h5M6 3.5 8.5 6 6 8.5" fill="none" stroke="var(--navy-deep)" stroke-width="1.6"/></svg>Sapiente</div>
      <div class="loc-item"><svg width="12" height="12" viewBox="0 0 12 12"><circle cx="6" cy="6" r="6" fill="#fff"/><path d="M3 6h5M6 3.5 8.5 6 6 8.5" fill="none" stroke="var(--navy-deep)" stroke-width="1.6"/></svg>Delectus</div>
    </div>
    <p class="loc-head" style="margin-top:18px">Molestiae</p>
    <div style="margin-top:11px;display:grid;row-gap:11px">
      <div class="loc-item"><svg width="12" height="12" viewBox="0 0 12 12"><circle cx="6" cy="6" r="6" fill="#fff"/><path d="M3 6h5M6 3.5 8.5 6 6 8.5" fill="none" stroke="var(--navy-deep)" stroke-width="1.6"/></svg>Voluptatibus</div>
      <div class="loc-item"><svg width="12" height="12" viewBox="0 0 12 12"><circle cx="6" cy="6" r="6" fill="#fff"/><path d="M3 6h5M6 3.5 8.5 6 6 8.5" fill="none" stroke="var(--navy-deep)" stroke-width="1.6"/></svg>Consequatur</div>
    </div>
  </div>
  <div class="abs" style="left:948px;top:3192px">
    <p class="loc-head">Assumenda</p>
    <div style="margin-top:11px;display:grid;row-gap:6px">
      <div class="loc-item"><svg width="12" height="12" viewBox="0 0 12 12"><circle cx="6" cy="6" r="6" fill="#fff"/><path d="M3 6h5M6 3.5 8.5 6 6 8.5" fill="none" stroke="var(--navy-deep)" stroke-width="1.6"/></svg>Harrowgate Vale</div>
      <div class="loc-item"><svg width="12" height="12" viewBox="0 0 12 12"><circle cx="6" cy="6" r="6" fill="#fff"/><path d="M3 6h5M6 3.5 8.5 6 6 8.5" fill="none" stroke="var(--navy-deep)" stroke-width="1.6"/></svg>Elmby</div>
      <div class="loc-item" style="margin-top:9px"><svg width="12" height="12" viewBox="0 0 12 12"><circle cx="6" cy="6" r="6" fill="#fff"/><path d="M3 6h5M6 3.5 8.5 6 6 8.5" fill="none" stroke="var(--navy-deep)" stroke-width="1.6"/></svg>Denounce</div>
      <div class="loc-item"><svg width="12" height="12" viewBox="0 0 12 12"><circle cx="6" cy="6" r="6" fill="#fff"/><path d="M3 6h5M6 3.5 8.5 6 6 8.5" fill="none" stroke="var(--navy-deep)" stroke-width="1.6"/></svg>Indignation</div>
    </div>
  </div>

  <p class="abs copyright">Copyrights © 2020 RW Construction. All rights reserved.</p>
  <nav class="footer-nav">
    <a style="left:701px" href="#">RESOURCES</a>
    <a style="left:782px" href="#">ABOUT</a>
    <a style="left:841px" href="#">SERVICES</a>
    <a style="left:909px" href="#">PORTFOLIO</a>
    <a style="left:989px" href="#">NEWS</a>
    <a style="left:1042px" href="#">CONTACT</a>
  </nav>

</div>
</body>
</html>
```